New business card design to go with our new logo

just want an eye-catching business card to go with our new logo. We are open to double sided or single sided. Just want it to have the following info on it. Whatever layout you think looks best.

First and Last Name
Title
Phone 801-555-0187
Address 312 W. Larkmoor Avenue Orem UT 84057
Email thecrew@meadowstailandkennel.example

Industry/Entity Type

Business

```html
<!DOCTYPE html>
<html lang="en">
<head>
<meta charset="utf-8">
<title>Meadows Tail &amp; Kennel — Business Card</title>
<link href="https://fonts.googleapis.com/css2?family=Roboto:wght@400;500&family=Roboto+Condensed:wght@500&display=swap" rel="stylesheet">
<style>
  :root {
    --stage: #2b2b2b;
    --card-white: #f4f4f4;
    --brand-blue: #2fa7da;
    --brand-orange: #f7924a;
    --ink: #4a4a4a;
    --white: #ffffff;
  }
  html, body {
    margin: 0;
    padding: 0;
    width: 1200px;
    height: 960px;
    overflow: hidden;
    background: var(--stage);
    font-family: "Roboto", Arial, sans-serif;
  }
  .canvas { position: relative; width: 1200px; height: 960px; }

  .card {
    position: absolute;
    width: 600px;
    height: 342px;
    border-radius: 18px;
    overflow: hidden;
  }
  .card--front { left: 314px; top: 113px; background: var(--card-white); }
  .card--back  { left: 311px; top: 472px; background: var(--brand-blue); }

  /* brand name block (front) */
  .brand-front {
    position: absolute;
    right: 32px;
    top: 36px;
    width: 200px;
    text-align: center;
    color: var(--brand-blue);
    font-family: "Roboto", Arial, sans-serif;
    font-weight: 500;
  }
  .brand-front__dot {
    display: block;
    width: 78px;
    height: 78px;
    margin: 0 auto 14px;
    border-radius: 50%;
    background: var(--brand-orange);
  }
  .brand-front__name { font-size: 30px; line-height: 32px; letter-spacing: 1px; }
  .brand-front__tag { font-size: 16px; line-height: 20px; }

  /* contact block */
  .contact { position: absolute; left: 27px; top: 166px; color: var(--ink); }
  .contact__name {
    font-family: "Roboto Condensed", Arial, sans-serif;
    font-weight: 500;
    font-size: 23px;
    line-height: 26px;
    color: var(--brand-blue);
    margin: 0;
  }
  .contact__title {
    font-family: "Roboto Condensed", Arial, sans-serif;
    font-weight: 500;
    font-size: 15px;
    line-height: 20px;
    color: var(--brand-orange);
    margin: 0 0 8px;
  }
  .contact__address { font-size: 14px; line-height: 18px; margin: 0 0 8px; }
  .contact__line { display: flex; align-items: center; gap: 9px; font-size: 14px; line-height: 20px; }
  .contact__line svg { width: 13px; height: 13px; fill: var(--brand-blue); }

  /* footer band */
  .footer-band { position: absolute; left: 0; bottom: 0; width: 600px; height: 26px; }
  .footer-url {
    position: absolute;
    left: 27px;
    bottom: 5px;
    color: var(--white);
    font-size: 14px;
    letter-spacing: 1.2px;
  }

  /* brand name block (back) */
  .brand-back {
    position: absolute;
    right: 34px;
    top: 232px;
    text-align: right;
    color: var(--white);
    font-family: "Roboto", Arial, sans-serif;
    font-weight: 500;
  }
  .brand-back__name { font-size: 40px; line-height: 42px; letter-spacing: 1px; }
  .brand-back__tag { font-size: 17px; line-height: 22px; }
</style>
</head>
<body>
<div class="canvas">

  <section class="card card--front">
    <div class="brand-front">
      <span class="brand-front__dot"></span>
      <div class="brand-front__name">MEADOWS</div>
      <div class="brand-front__tag">Tail &amp; Kennel</div>
    </div>

    <div class="contact">
      <p class="contact__name">DANA REYES</p>
      <p class="contact__title">CEO/FOUNDER</p>
      <p class="contact__address">312 W. Larkmoor Avenue<br>Orem UT 84057</p>
      <div class="contact__line">
        <svg viewBox="0 0 24 24" aria-hidden="true"><path d="M6.6 10.8a15.1 15.1 0 0 0 6.6 6.6l2.2-2.2c.3-.3.7-.4 1-.2 1.1.4 2.3.6 3.6.6.6 0 1 .4 1 1V20c0 .6-.4 1-1 1C10.6 21 3 13.4 3 4c0-.6.4-1 1-1h3.5c.6 0 1 .4 1 1 0 1.3.2 2.5.6 3.6.1.3 0 .7-.2 1z"/></svg>
        <span>801-555-0187</span>
      </div>
      <div class="contact__line">
        <svg viewBox="0 0 24 24" aria-hidden="true"><path d="M2 5h20v14H2z M2 5l10 8 10-8" /><path d="M3 6l9 7 9-7" fill="#f4f4f4"/></svg>
        <span>thecrew@meadowstailandkennel.example</span>
      </div>
    </div>

    <svg class="footer-band" viewBox="0 0 600 26" aria-hidden="true">
      <path d="M0 0 H288 C306 0 310 12 330 12 H600 V26 H0 Z" fill="var(--brand-blue)"/>
      <path d="M300 4 C312 4 316 6 332 6 H600 V12 H330 C312 12 310 4 300 4 Z" fill="var(--brand-orange)"/>
    </svg>
    <span class="footer-url">www.meadowstailandkennel.example</span>
  </section>

  <section class="card card--back">
    <div class="brand-back">
      <div class="brand-back__name">MEADOWS</div>
      <div class="brand-back__tag">Tail &amp; Kennel</div>
    </div>
  </section>

</div>
</body>
</html>
```